"Harborline Inc." Needs a Logo Design and Business Card

The name of the company is "Harborline Inc."
Our Business decription, which should appear on the front of the Business Card along with the logo and business name is:
"Boutique Global Procurement and Management Services"
We offer the following SERVICES that should be listed on the back of the Business Card :
"Consultants"
"Management"
"Business Research & Development"
"Sourcing Agent"
"Distributors"
We would like to see designs that use the colors
burnt orange and,
stainless steel
Business card designs should be innovatively modern and contemporary
Telephone number and email address should be on the back of the card
The name of the firm is "Harborline Inc.
Steel

```html
<!DOCTYPE html>
<html lang="en">
<head>
<meta charset="utf-8">
<title>Harborline Inc. – Business Card</title>
<link rel="stylesheet" href="https://fonts.googleapis.com/css2?family=Open+Sans:wght@400;600;700&family=Questrial&display=swap">
<style>
  :root {
    --burnt-orange: #d4541a;
    --burnt-orange-deep: #b8430c;
    --peach: #f6c9a4;
    --steel-bg: #e6e7ea;
    --card-white: #ffffff;
    --ink: #2f343c;
    --ink-soft: #3d4148;
    --wave-front: #e58a3a;
    --wave-back: #f7d3a6;
  }
  * { box-sizing: border-box; margin: 0; padding: 0; }
  html, body { width: 1200px; height: 934px; overflow: hidden; }
  body {
    background: var(--steel-bg);
    font-family: "Open Sans", Arial, sans-serif;
    position: relative;
  }
  .card {
    position: absolute;
    left: 240px;
    width: 720px;
    height: 412px;
    overflow: hidden;
    box-shadow: 0 6px 18px rgba(0,0,0,0.12);
  }
  .card--front { top: 35px; background: linear-gradient(160deg, #de5c1f 0%, var(--burnt-orange) 45%, var(--burnt-orange-deep) 100%); }
  .card--back { top: 487px; background: var(--card-white); }

  .wave-area { position: absolute; }
  .card--front .wave-area {
    left: 0; right: 0; bottom: 0; height: 80px;
    background: linear-gradient(180deg, rgba(229,138,58,0) 0%, var(--wave-front) 100%);
  }
  .card--back .wave-area {
    right: 0; bottom: 0; width: 460px; height: 300px;
    background: linear-gradient(155deg, rgba(247,211,166,0) 40%, var(--wave-back) 100%);
  }

  .edge-tab { position: absolute; left: 0; width: 22px; }
  .card--front .edge-tab { top: 62px; height: 78px; background: #f1f1f1; }
  .card--back .edge-tab { top: 205px; height: 80px; background: var(--burnt-orange); }

  .brand-name {
    position: absolute;
    font-family: "Open Sans", Arial, sans-serif;
    font-weight: 700;
    font-size: 44px;
    letter-spacing: 0.5px;
    line-height: 1;
  }
  .card--front .brand-name { left: 78px; top: 62px; color: #ffffff; }
  .card--back .brand-name { left: 70px; top: 140px; color: var(--burnt-orange); }

  .tagline {
    position: absolute;
    font-size: 17px;
    font-weight: 600;
    line-height: 1.15;
  }
  .card--front .tagline { left: 80px; top: 116px; color: var(--peach); }
  .card--back .tagline { left: 92px; top: 196px; color: var(--ink-soft); }

  .services {
    position: absolute;
    left: 96px;
    top: 175px;
    list-style: none;
    font-family: "Questrial", "Century Gothic", sans-serif;
    font-size: 23px;
    letter-spacing: 1.2px;
    color: #ffffff;
    line-height: 40px;
  }

  .person { position: absolute; left: 470px; top: 62px; }
  .person__name { font-size: 25px; font-weight: 700; color: var(--ink); letter-spacing: 0.5px; }
  .person__role { font-size: 18px; color: var(--ink-soft); margin-left: 18px; margin-top: -2px; }

  .contact {
    position: absolute;
    left: 92px;
    top: 272px;
    font-size: 18px;
    line-height: 24px;
    color: var(--ink-soft);
    font-style: normal;
  }
  .contact__label { color: var(--burnt-orange); }
</style>
</head>
<body>

<section class="card card--front" aria-label="Business card back: services">
  <div class="wave-area" role="img" aria-label="Decorative orange wave ornament along the bottom edge"></div>
  <span class="edge-tab"></span>
  <h1 class="brand-name">Harborline Inc.</h1>
  <p class="tagline">Boutique Global Procurement<br>and Management Services</p>
  <ul class="services">
    <li>Consultants • Management</li>
    <li>Business Research &amp; Development</li>
    <li>Sourcing Agent • Distributors</li>
  </ul>
</section>

<section class="card card--back" aria-label="Business card front: contact">
  <div class="wave-area" role="img" aria-label="Decorative soft orange swoosh ornament in the lower right corner"></div>
  <div class="person">
    <p class="person__name">DANIEL MARSH</p>
    <p class="person__role">Sales Manager</p>
  </div>
  <span class="edge-tab"></span>
  <h2 class="brand-name">Harborline Inc.</h2>
  <p class="tagline">Boutique Global Procurement<br>and Management Services</p>
  <address class="contact">
    <span class="contact__label">Phone:</span> 0400 218 774<br>
    <span class="contact__label">Email:</span> daniel@harborline.example<br>
    27 Bayview Parade<br>
    Seacliff NSW 2000
  </address>
</section>

</body>
</html>
```